B2B Manufacturer - Trade Show Booth Design

This is a 2-part project. The business is a custom spring manufacturer. I would like our existing logo cleaned up and converted to vector art and I would like graphics designed for a trade show booth backdrop and monitor stand. Refer to BrightwellCoilWorks.com, the corporate website, for colors and for reference information. See attached for logo, booth rendering and booth template for dimensions and artwork requirements. THE PRIMARY CREATIVE ELEMENTS IN THIS PROJECT WILL BE COLOR CHOICE, CONTRAST, THE BACKGROUND GRAPHIC FOR ITEM #2 AND GENERAL LAYOUT.

Target Market(s)

B2B - Engineers, Buyers, Supply Chain Managers

Industry/Entity Type

Manufaturing - Springs and Wire Forms

Font styles to use
Sans Serif

Requirements
Must have
• I prefer rich, dark high-contrast themes/designs. See website for general color scheme reference. Template Item #1 - TEXT: "Custom Springs & Wire Forms". Template Item #3 (Front) - I will be mounting a 43-inch vertical display on the front so this area will get a logo at the top. #1 - #2 - Dark, rich color that incorporates a unique and interesting background graphic. Logo at top with "Brightwell Coil Works" underneath logo. #3 Front - Logo above TV/Display. I will have a vertical signage display so no text under the TV spot. #3 Back - Open to ideas. #3 Pedastal Front - Logo with "Brightwell Coil Works " under logo. #4 Front - Logo with "Brightwell Coil Works " under logo. #4 Sides - Blank
Nice to have
• I have many images to work with and would like to look at both color and Black-and-white variations.

```html
<!DOCTYPE html>
<html lang="en">
<head>
<meta charset="utf-8">
<title>Brightwell Coil Works – Trade Show Booth Graphics</title>
<link rel="stylesheet" href="https://fonts.googleapis.com/css2?family=Syncopate:wght@700&family=Open+Sans:wght@400;600;700&display=swap">
<style>
  :root {
    --page: #ffffff;
    --panel-dark: #161616;
    --panel-mid: #474747;
    --hidden-zone: #ececec;
    --hidden-band: #8c8c8c;
    --ink-white: #ffffff;
    --ink-grey: #3a3a3a;
    --label-orange: #e8641c;
    --mark-grey: #9a9a9a;
    --steel-light: #8e8e8e;
    --steel-dark: #2a2a2a;
  }
  html, body {
    margin: 0;
    padding: 0;
    width: 1200px;
    height: 1018px;
    overflow: hidden;
    background: var(--page);
  }
  .booth-sheet { display: block; width: 1200px; height: 1018px; }
  .brand-name, .brand-mark { font-family: "Syncopate", sans-serif; font-weight: 700; fill: var(--ink-white); }
  .mark-dot { fill: var(--mark-grey); }
  .banner-text { font-family: "Open Sans", sans-serif; font-weight: 600; fill: var(--ink-white); }
  .zone-note { font-family: "Open Sans", sans-serif; font-weight: 400; fill: var(--ink-grey); }
  .zone-note-light { font-family: "Open Sans", sans-serif; font-weight: 400; fill: #d8d8d8; }
  .face-label { font-family: "Open Sans", sans-serif; font-weight: 700; fill: var(--label-orange); }
  .hidden-zone { fill: var(--hidden-zone); }
  .guide { fill: none; stroke: #3a2a22; stroke-width: 0.6; stroke-dasharray: 2 2; opacity: 0.6; }
</style>
</head>
<body>
<svg class="booth-sheet" viewBox="0 0 1200 1018" xmlns="http://www.w3.org/2000/svg" role="img" aria-label="Brightwell Coil Works trade show booth artwork layout">
  <defs>
    <radialGradient id="darkPanel" cx="50%" cy="50%" r="65%">
      <stop offset="0" stop-color="var(--panel-mid)"/>
      <stop offset="1" stop-color="var(--panel-dark)"/>
    </radialGradient>
    <linearGradient id="steelWash" x1="0" y1="0" x2="1" y2="1">
      <stop offset="0" stop-color="var(--steel-dark)"/>
      <stop offset="0.5" stop-color="#3e3e3e"/>
      <stop offset="0.8" stop-color="#4a4a4a"/>
      <stop offset="1" stop-color="var(--steel-dark)"/>
    </linearGradient>
    <linearGradient id="bandWash" x1="0" y1="0" x2="1" y2="0">
      <stop offset="0" stop-color="#838383"/>
      <stop offset="1" stop-color="#999999"/>
    </linearGradient>
  </defs>

  <!-- Tower -->
  <g class="tower">
    <path d="M67.5 121 a29 29 0 0 1 29 -29 h133 a29 29 0 0 1 29 29 v438 h-191 z" fill="url(#darkPanel)"/>
    <path class="hidden-zone" d="M67.5 559 h191 v157 a24 24 0 0 1 -24 24 h-143 a24 24 0 0 1 -24 -24 z"/>
    <rect class="guide" x="81" y="103" width="164" height="625" rx="22"/>
    <text class="zone-note" x="163" y="657" font-size="18" text-anchor="middle">Invisible</text>
  </g>

  <!-- Monitor stand -->
  <g class="monitor-stand">
    <path d="M267 359 a29 29 0 0 1 29 -29 h134 a29 29 0 0 1 29 29 v290 h-192 z" fill="url(#steelWash)" role="img" aria-label="Silver swoosh background graphic"/>
    <g class="logo-slot">
      <circle class="mark-dot" cx="333" cy="395" r="7"/>
      <text class="brand-mark" x="346" y="403" font-size="20" textLength="60" lengthAdjust="spacingAndGlyphs">BCW</text>
    </g>
    <rect class="hidden-zone" x="276" y="430" width="174" height="127"/>
    <text class="zone-note" x="363" y="487" font-size="20" text-anchor="middle">22″~40″</text>
    <text class="zone-note" x="363" y="516" font-size="20" text-anchor="middle">TV</text>
    <path class="hidden-zone" d="M267 649 h192 v67 a24 24 0 0 1 -24 24 h-144 a24 24 0 0 1 -24 -24 z"/>
    <text class="zone-note" x="364" y="690" font-size="18" text-anchor="middle">Invisible</text>
  </g>

  <!-- Header banner -->
  <g class="header-banner">
    <rect x="628" y="75" width="346" height="83" fill="url(#steelWash)" role="img" aria-label="Silver swoosh background graphic"/>
    <text class="banner-text" x="801" y="124" font-size="17" text-anchor="middle" textLength="272" lengthAdjust="spacingAndGlyphs">CUSTOM SPRINGS &amp; WIRE FORMS</text>
  </g>

  <!-- Main backdrop -->
  <g class="backdrop">
    <rect x="467" y="170" width="667" height="512" fill="url(#steelWash)" role="img" aria-label="Silver swoosh background graphic"/>
    <rect class="guide" x="493" y="190" width="614" height="470" rx="40"/>
    <g class="logo-slot">
      <circle class="mark-dot" cx="742" cy="342" r="20"/>
      <text class="brand-mark" x="774" y="362" font-size="56" textLength="146" lengthAdjust="spacingAndGlyphs">BCW</text>
    </g>
    <text class="brand-name" x="801" y="482" font-size="40" text-anchor="middle" textLength="359" lengthAdjust="spacingAndGlyphs">BRIGHTWELL</text>
    <text class="brand-name" x="801" y="519" font-size="24" text-anchor="middle" textLength="300" lengthAdjust="spacingAndGlyphs">COIL WORKS</text>
  </g>

  <!-- Pedestal -->
  <g class="pedestal">
    <path d="M111 749 H444 L487.5 893 V949 H67.5 V893 Z" fill="url(#darkPanel)"/>
    <path class="guide" d="M127 765 H428 L467 893 V935 H93 V893 Z"/>
    <line x1="200" y1="765" x2="200" y2="935" stroke="#2a3550" stroke-width="0.6"/>
    <line x1="356" y1="765" x2="356" y2="935" stroke="#2a3550" stroke-width="0.6"/>
    <g class="logo-slot">
      <circle class="mark-dot" cx="243" cy="818" r="12"/>
      <text class="brand-mark" x="263" y="831" font-size="34" textLength="80" lengthAdjust="spacingAndGlyphs">BCW</text>
    </g>
    <text class="brand-name" x="278" y="883" font-size="14" text-anchor="middle" textLength="120" lengthAdjust="spacingAndGlyphs">BRIGHTWELL</text>
    <text class="brand-name" x="278" y="896" font-size="9" text-anchor="middle" textLength="100" lengthAdjust="spacingAndGlyphs">COIL WORKS</text>
  </g>

  <!-- Counter wrap -->
  <g class="counter">
    <rect x="534" y="697" width="600" height="252" fill="url(#darkPanel)"/>
    <rect x="534" y="697" width="600" height="32" fill="url(#bandWash)"/>
    <rect x="534" y="917" width="600" height="32" fill="url(#bandWash)"/>
    <line x1="534" y1="713" x2="800" y2="713" stroke="#bdbdbd" stroke-width="0.6"/>
    <line x1="868" y1="713" x2="1134" y2="713" stroke="#bdbdbd" stroke-width="0.6"/>
    <line x1="534" y1="933" x2="800" y2="933" stroke="#bdbdbd" stroke-width="0.6"/>
    <line x1="868" y1="933" x2="1134" y2="933" stroke="#bdbdbd" stroke-width="0.6"/>
    <text class="zone-note-light" x="834" y="718" font-size="10" text-anchor="middle">Invisible</text>
    <text class="zone-note-light" x="834" y="938" font-size="10" text-anchor="middle">Invisible</text>
    <rect class="guide" x="644" y="740" width="104" height="167"/>
    <rect class="guide" x="748" y="740" width="172" height="167"/>
    <rect class="guide" x="944" y="740" width="78" height="167"/>

    <g class="side-face">
      <circle class="mark-dot" cx="662" cy="819" r="6"/>
      <text class="brand-mark" x="672" y="826" font-size="18" textLength="46" lengthAdjust="spacingAndGlyphs">BCW</text>
      <text class="brand-name" x="686" y="860" font-size="7.5" text-anchor="middle" textLength="64" lengthAdjust="spacingAndGlyphs">BRIGHTWELL</text>
      <text class="brand-name" x="686" y="867" font-size="4.5" text-anchor="middle" textLength="54" lengthAdjust="spacingAndGlyphs">COIL WORKS</text>
      <text class="face-label" x="683" y="906" font-size="10" text-anchor="middle">Side</text>
    </g>
    <g class="front-face">
      <circle class="mark-dot" cx="798" cy="787" r="10"/>
      <text class="brand-mark" x="814" y="799" font-size="28" textLength="66" lengthAdjust="spacingAndGlyphs">BCW</text>
      <text class="brand-name" x="835" y="854" font-size="16" text-anchor="middle" textLength="140" lengthAdjust="spacingAndGlyphs">BRIGHTWELL</text>
      <text class="brand-name" x="835" y="868" font-size="9" text-anchor="middle" textLength="119" lengthAdjust="spacingAndGlyphs">COIL WORKS</text>
      <text class="face-label" x="833" y="906" font-size="10" text-anchor="middle">Front</text>
    </g>
    <g class="side-face">
      <circle class="mark-dot" cx="959" cy="823" r="6"/>
      <text class="brand-mark" x="969" y="830" font-size="18" textLength="46" lengthAdjust="spacingAndGlyphs">BCW</text>
      <text class="brand-name" x="983" y="860" font-size="7.5" text-anchor="middle" textLength="64" lengthAdjust="spacingAndGlyphs">BRIGHTWELL</text>
      <text class="brand-name" x="983" y="867" font-size="4.5" text-anchor="middle" textLength="54" lengthAdjust="spacingAndGlyphs">COIL WORKS</text>
      <text class="face-label" x="981" y="906" font-size="10" text-anchor="middle">Side</text>
    </g>
  </g>
</svg>
</body>
</html>
```